USB Stick Gewinnspiel
Zielgruppe
Männer, Technikinteressierte
Aufgabenstellung
Design für ein Gewinnspiel bei dem es 100 USB Sticks, 32 GB (mit die kleinsten USB Sticks der Welt) zu gewinnen gibt.
Menüpunkte: Startseite, Teilnahmebedingungen, Preisdetails, Teilnehmen, Datenschutz.
Es soll eine Intro-Seite auf der der Preis groß heraus gestellt ist gestaltet werden mit den entsprechenden Menüpunkten sowie eine Template-Seite in der wir dann alle notwendigen Inhalte einfügen können. Von der Gestaltung her seid Ihr frei. Klein ist jedoch sexy, daher darf der USB Stick mit einer sexy Dame präsentiert werden die Männerherzen höher schlagen läßt.
Gewinnspiele von uns finden Sie auf www.glueckspfad.de damit Sie sich ein Bild über die bisherigen Gewinnspiele machen können.
WICHTIG: Es soll nur die Eingangsseite und eine Template Seite erstellt werden. Die komplette Programmierung bzw. Füllung mit Inhalten wird von uns gemacht! Für die Templateseite wäre eine Breite von 500 Pixeln oder mehr im Bereich wo wir Inhalte einfügen können wünschenswert.
„Normales altbackenes“ HTML mit Tabellen ohne großen CSS Schnick-Schnack würden wir bevorzugen da es für uns einfacher zum Bearbeiten ist.
Das Gewinnspiel wird später auf einer Subdomain laufen und hat somit keinen Domainnamen den man im Titel darstellen kann oder muss.
Das fertige Layout soll dann als geschnittene HTML Datei mit verlinkten Grafiken geliefert werden.

```html
<!DOCTYPE html>
<html lang="de">
<head>
<meta charset="utf-8">
<title>USB-Gewinnspiel</title>
<link rel="stylesheet" href="https://fonts.googleapis.com/css2?family=Arimo:wght@400;700&family=Open+Sans:wght@400;600;700&family=Yanone+Kaffeesatz:wght@700&display=swap">
<style>
:root{
  --bg-light:#ffd0a0;
  --bg-mid:#fdb27a;
  --bg-dark:#f98f5a;
  --orange:#f7883a;
  --orange-deep:#ee6b1c;
  --orange-pale:#fbb47c;
  --nav-active:#ff5a00;
  --gold:#e0b43a;
  --gold-dark:#7a5a10;
  --white:#ffffff;
  --panel:#f7f7f7;
  --text:#111111;
  --muted:#555555;
  --heading-red:#d8141c;
  --ribbon:#c8102e;
  --badge:#f2b705;
  --badge-edge:#e8540f;
  --line:#d9d9d9;
}
*{box-sizing:border-box;margin:0;padding:0}
html,body{width:1200px;height:1200px;overflow:hidden}
body{
  position:relative;
  font-family:"Open Sans",sans-serif;
  color:var(--text);
  background:radial-gradient(ellipse 70% 60% at 50% 60%,var(--bg-light) 0%,var(--bg-mid) 60%,var(--bg-dark) 100%);
}
.site-title{
  position:absolute;top:26px;left:0;width:1200px;text-align:center;
  font-family:"Yanone Kaffeesatz",sans-serif;font-weight:700;font-size:78px;letter-spacing:1px;
  color:var(--gold);
  text-shadow:0 2px 0 var(--gold-dark);
}
.page{
  position:absolute;left:129px;top:141px;width:942px;height:862px;
  background:var(--panel);border-radius:10px;
  box-shadow:0 0 40px rgba(255,255,255,.6);
  overflow:hidden;
}
.nav-bar{
  position:absolute;left:0;top:0;width:100%;height:36px;
  background:linear-gradient(var(--orange-pale),var(--orange) 60%,var(--orange-deep));
}
.main-nav{
  position:absolute;top:8px;left:139px;display:flex;gap:0;
  font-family:"Arimo",sans-serif;font-weight:700;font-size:18px;color:var(--white);
}
.main-nav a{color:inherit;text-decoration:none;margin-right:26px}
.main-nav a.is-active{color:var(--nav-active)}
.header{
  position:absolute;left:0;top:36px;width:100%;height:200px;
  background:linear-gradient(var(--white),var(--white) 70%,var(--panel));
}
.brand{
  position:absolute;left:35px;top:110px;
  font-family:"Open Sans",sans-serif;font-weight:700;font-size:38px;color:var(--ribbon);
}
.photo-circle{
  position:absolute;width:160px;height:160px;border-radius:50%;
  background:radial-gradient(circle at 50% 40%,#9a9ea6,#5d626c);
  box-shadow:0 0 18px 6px rgba(255,170,190,.55);
}
.photo-circle.one{left:260px;top:51px}
.photo-circle.two{left:544px;top:51px}
.product-shot{
  position:absolute;left:710px;top:55px;width:210px;height:150px;border-radius:14px;
  background:linear-gradient(135deg,#e8e8e8,#3a3a3a 55%,#1c1c1c);opacity:.85;
}
.ribbon{position:absolute;left:-10px;top:-8px;width:170px;height:170px}
.badge{position:absolute;left:985px;top:115px;width:128px;height:128px}
.badge-text{
  position:absolute;left:985px;top:138px;width:128px;text-align:center;color:var(--white);
  font-family:"Arimo",sans-serif;font-weight:700;line-height:1;
}
.badge-text .count{font-size:28px;font-weight:400}
.badge-text .size{font-size:30px;font-style:italic}
.badge-text .kind{font-size:13px}
.cta{
  position:absolute;left:136px;top:262px;width:282px;height:78px;border-radius:10px;
  background:linear-gradient(#f4f4f4,#cfcfcf);border:4px solid #c8c8c8;
  box-shadow:inset 0 0 0 2px #fff,0 1px 3px rgba(0,0,0,.3);
}
.cta svg{position:absolute;left:22px;top:16px}
.cta-text{
  position:absolute;left:66px;top:12px;text-align:center;width:200px;
  font-size:21px;line-height:25px;color:#333;
}
.cta-text strong{font-weight:700}
.entry-heading{
  position:absolute;left:35px;top:368px;font-family:"Arimo",sans-serif;
  font-size:20px;color:var(--heading-red);text-decoration:underline;text-decoration-color:#bbb;
}
.intro{position:absolute;left:33px;top:413px;font-size:15px}
.intro strong{font-weight:600}
.entry-form{position:absolute;left:35px;top:453px;font-size:14px}
.field-row{display:flex;align-items:flex-start;height:34px}
.field-row label{width:124px;padding-top:0}
.input{border:2px solid var(--text);background:var(--white);height:28px}
.input.text{width:192px}
.input.wide{width:275px}
.select{
  height:30px;border:2px solid var(--text);background:#fafafa;position:relative;
  margin-right:5px;font-size:13px;padding:4px 6px;
}
.select::after{content:"";position:absolute;right:6px;top:11px;border:4px solid transparent;border-top:5px solid #333}
.select.title{width:66px}
.select.day{width:53px}
.select.month{width:53px}
.select.year{width:72px}
.submit{
  position:absolute;left:35px;top:678px;border:2px solid var(--text);background:var(--white);
  font-size:15px;padding:3px 6px;
}
.facts-label{
  position:absolute;left:525px;top:261px;font-size:20px;color:#b5b5b5;
}
.facts{
  position:absolute;left:524px;top:285px;width:376px;height:233px;
  background:var(--white);border:1px solid var(--line);border-radius:10px;
  padding:18px 18px 0 36px;
}
.facts li{font-size:13.5px;line-height:15px;color:var(--muted);margin-bottom:15px}
.footer-bar{
  position:absolute;left:0;top:826px;width:100%;height:36px;
  background:linear-gradient(var(--orange-pale),var(--orange) 60%,var(--orange-deep));
}
.footer-nav{
  position:absolute;right:14px;top:10px;font-family:"Arimo",sans-serif;font-size:13px;color:var(--white);
}
.footer-nav a{color:inherit;text-decoration:none;margin-left:4px}
</style>
</head>
<body>
<h1 class="site-title">USB-Gewinnspiel</h1>

<div class="page">
  <div class="header">
    <div class="brand">Taschenbit</div>
    <div class="photo-circle one" role="img" aria-label="Foto: Finger halten einen winzigen USB-Stick"></div>
    <div class="photo-circle two" role="img" aria-label="Foto: Hand steckt USB-Stick mit Schlüsselring"></div>
    <div class="product-shot" role="img" aria-label="Produktfoto: Mini-USB-Stick mit Kappe und Kette"></div>
  </div>
  <div class="nav-bar"></div>
  <nav class="main-nav">
    <a href="#">Startseite</a>
    <a href="#">Teilnahmebedingungen</a>
    <a href="#">Preisdetails</a>
    <a href="#" class="is-active">Teilnehmen</a>
    <a href="#">Datenschutz</a>
  </nav>

  <a class="cta" href="#">
    <svg width="34" height="40" viewBox="0 0 34 40">
      <path d="M2 2 L17 14 L32 2 L32 12 L17 24 L2 12Z" fill="#f4924a"/>
      <path d="M2 16 L17 28 L32 16 L32 26 L17 38 L2 26Z" fill="#ee6b1c"/>
    </svg>
    <span class="cta-text"><strong>JETZT MITMACHEN</strong><br>KOSTENLOS !</span>
  </a>

  <h2 class="entry-heading">Gewinnspielteilnahme:</h2>
  <p class="intro">Bitte tragen Sie sich nun für das <strong>kostenlose</strong> Gewinnspiel ein:</p>

  <form class="entry-form">
    <div class="field-row"><label>Anrede</label><span class="select title">-</span></div>
    <div class="field-row"><label>Vorname</label><span class="input text"></span></div>
    <div class="field-row"><label>Name</label><span class="input text"></span></div>
    <div class="field-row"><label>Geburtsdatum</label><span class="select day">-</span><span class="select month">-</span><span class="select year">-</span></div>
    <div class="field-row"><label>E-Mail</label><span class="input wide"></span></div>
  </form>
  <button class="submit" type="button">Zur Seite 2</button>

  <p class="facts-label">kurzer Einblick:</p>
  <ul class="facts">
    <li>Gigantische 32 GB Speicherkapazität!</li>
    <li>Winziger USB-Speicherstick mit Öse für die Befesti-<br>gung am Schlüsselbund</li>
    <li>Superschneller Datentransfer über USB2.0-<br>Schnittstelle</li>
    <li>Staub- und wasserdichter Korpus aus leichtem<br>Kunststoff</li>
    <li>Hauchdünne 21 x 16 x 16 mm, federleichte 2 g<br>Mit der kleinste USB-Stick der Welt!</li>
  </ul>

  <div class="footer-bar">
    <nav class="footer-nav">
      <a href="#">Startseite</a> <a href="#">Teilnahmebedingungen</a> <a href="#">Preisdetails</a> <a href="#">Teilnehmen</a> <a href="#">Datenschutz</a> <a href="#">Impressum</a>
    </nav>
  </div>
</div>

<svg class="ribbon" style="left:119px;top:133px" viewBox="0 0 170 170" aria-hidden="true">
  <path d="M10 90 L95 5 L148 5 L10 143Z" fill="var(--ribbon)"/>
  <path d="M95 5 L148 5 L150 0 L100 0Z" fill="#8a0a1e"/>
  <text x="0" y="0" transform="translate(42 108) rotate(-45)" fill="#fff" font-family="Georgia,serif" font-weight="700" font-size="17">KOSTENLOS</text>
</svg>

<svg class="badge" viewBox="0 0 128 128" aria-hidden="true">
  <polygon fill="var(--badge-edge)" points="64,2 72,14 85,5 89,20 104,15 103,30 118,30 111,44 125,50 114,61 125,72 112,80 119,94 104,96 106,111 91,108 87,123 74,115 64,126 54,115 41,123 37,108 22,111 24,96 9,94 16,80 3,72 14,61 3,50 17,44 10,30 25,30 24,15 39,20 43,5 56,14"/>
  <circle cx="64" cy="64" r="50" fill="var(--badge)"/>
</svg>
<div class="badge-text">
  <div class="count">100x</div>
  <div class="size">32 GB</div>
  <div class="kind">USB-Sticks</div>
</div>
</body>
</html>
```